Quill Forge Solutions
Bold and Unique
Project: Quill Forge Solutions
Quill Forge Solutions -
Creative Brief
Simple
Gary Holbrook
Owner / IT Consultant
Gary@TheQuillForge.com
www.TheQuillForge.com
Please use either black and white, or black and red if you can... but if you find something that works better, than that works too!! Please be as creative and bold as possible!

```html
<!DOCTYPE html>
<html lang="en">
<head>
<meta charset="utf-8">
<title>Quill Forge Solutions Stationery</title>
<link href="https://fonts.googleapis.com/css2?family=Arimo:wght@400;700&display=swap" rel="stylesheet">
<style>
  :root {
    --ink: #111111;
    --ink-soft: #3a3a3a;
    --grey: #8a8a8a;
    --mist: #ececec;
    --paper: #ffffff;
    --page-bg: #ffffff;
  }
  * { box-sizing: border-box; margin: 0; padding: 0; }
  html, body { width: 1200px; height: 1052px; overflow: hidden; background: var(--page-bg); }
  body { position: relative; font-family: "Arimo", Arial, sans-serif; color: var(--ink); }

  .brand { display: flex; align-items: center; gap: 10px; font-family: "Arimo", Arial, sans-serif; font-weight: 700; text-transform: uppercase; letter-spacing: 0.12em; white-space: nowrap; }
  .brand-dot { border-radius: 50%; flex: none; }

  /* Letterhead */
  .letterhead { position: absolute; left: 83px; top: 50px; width: 715px; height: 885px; background: var(--paper); box-shadow: 0 0 3px rgba(0,0,0,.35); overflow: hidden; }
  .letterhead-band { position: absolute; left: 0; top: 0; width: 100%; height: 120px; }
  .letterhead .brand { position: absolute; left: 24px; top: 28px; color: var(--paper); font-size: 22px; }
  .letterhead .brand-dot { width: 46px; height: 46px; background: var(--paper); }
  .letterhead-mark { position: absolute; left: 210px; top: 190px; width: 440px; height: 440px; border-radius: 50%; background: radial-gradient(circle at 40% 35%, #f7f7f7, #e6e6e6); }
  .letterhead-contact { position: absolute; right: 36px; bottom: 100px; text-align: right; font-size: 13px; line-height: 1.35; color: var(--ink); font-style: normal; }
  .letterhead-footer { position: absolute; left: 0; bottom: 0; width: 100%; height: 110px; }

  /* Business cards */
  .card { position: absolute; box-shadow: 0 0 2px rgba(0,0,0,.4); overflow: hidden; }
  .card-front { left: 908px; top: 41px; width: 180px; height: 138px; background: var(--ink); display: flex; align-items: center; justify-content: center; }
  .card-front .brand { flex-direction: column; gap: 8px; color: var(--paper); font-size: 11px; text-align: center; }
  .card-front .brand-dot { width: 34px; height: 34px; background: var(--paper); }

  .card-back-light { left: 908px; top: 195px; width: 180px; height: 86px; background: var(--paper); text-align: center; padding-top: 14px; font-size: 9px; line-height: 1.35; color: var(--ink-soft); }
  .card-strip { left: 908px; top: 300px; width: 180px; height: 24px; background: var(--ink); color: var(--paper); font-size: 6px; letter-spacing: 0.12em; text-transform: uppercase; display: flex; align-items: center; padding-left: 10px; }

  .card-dark { left: 908px; top: 358px; width: 248px; height: 165px; background: linear-gradient(160deg, #2b2b2b, var(--ink) 55%); color: var(--paper); }
  .card-dark .brand { position: absolute; left: 16px; top: 20px; font-size: 9.5px; letter-spacing: 0.08em; gap: 9px; }
  .card-dark .brand-dot { width: 30px; height: 30px; background: var(--paper); }
  .card-dark-details { position: absolute; left: 0; right: 0; top: 70px; text-align: center; font-size: 9px; line-height: 1.35; color: #dddddd; }
  .card-dark-web { position: absolute; right: 14px; bottom: 10px; font-size: 7px; letter-spacing: 0.12em; text-transform: uppercase; color: #dddddd; }

  /* Standalone logo */
  .logo-lockup { position: absolute; left: 815px; top: 800px; width: 280px; display: flex; flex-direction: column; align-items: center; }
  .logo-lockup .brand { flex-direction: column; gap: 16px; color: var(--ink-soft); font-size: 16px; letter-spacing: 0.1em; }
  .logo-lockup .brand-dot { width: 70px; height: 70px; background: var(--ink-soft); }
</style>
</head>
<body>

<section class="letterhead" aria-label="Letterhead">
  <svg class="letterhead-band" viewBox="0 0 715 120" preserveAspectRatio="none" aria-hidden="true">
    <defs>
      <linearGradient id="bandGrad" x1="0" y1="0" x2="1" y2="0">
        <stop offset="0" stop-color="#111"/>
        <stop offset="0.6" stop-color="#2e2e2e"/>
        <stop offset="1" stop-color="#6a6a6a"/>
      </linearGradient>
    </defs>
    <path d="M0 0 H715 V62 C500 74 260 88 0 108 Z" fill="url(#bandGrad)"/>
    <path d="M0 108 C260 88 500 74 715 62 V70 C500 82 260 98 0 118 Z" fill="#c8c8c8"/>
  </svg>
  <div class="brand"><span class="brand-dot"></span>Quill Forge Solutions</div>

  <div class="letterhead-mark" role="img" aria-label="Faint circular brand watermark"></div>

  <address class="letterhead-contact">
    Tel: 555-014-2290<br>
    Gary@TheQuillForge.com<br>
    www.TheQuillForge.com
  </address>

  <svg class="letterhead-footer" viewBox="0 0 715 110" preserveAspectRatio="none" aria-hidden="true">
    <defs>
      <linearGradient id="footGrad" x1="0" y1="0" x2="1" y2="0">
        <stop offset="0" stop-color="#111"/>
        <stop offset="0.7" stop-color="#333"/>
        <stop offset="1" stop-color="#777"/>
      </linearGradient>
    </defs>
    <path d="M0 28 C220 52 480 62 715 50 V110 H0 Z" fill="#cfcfcf"/>
    <path d="M0 40 C220 62 480 72 715 60 V110 H0 Z" fill="url(#footGrad)"/>
  </svg>
</section>

<div class="card card-front" aria-label="Business card front">
  <div class="brand"><span class="brand-dot"></span>Quill Forge<br>Solutions</div>
</div>

<div class="card card-back-light" aria-label="Business card back">
  Gary Holbrook<br>
  Owner/IT Consultant<br>
  Tel: 555-014-2290<br>
  Gary@TheQuillForge.com
</div>

<div class="card card-strip">www.TheQuillForge.com</div>

<div class="card card-dark" aria-label="Business card dark">
  <div class="brand"><span class="brand-dot"></span>Quill Forge Solutions</div>
  <div class="card-dark-details">
    Gary Holbrook<br>
    Owner/IT Consultant<br>
    Tel: 555-014-2290<br>
    Gary@TheQuillForge.com
  </div>
  <div class="card-dark-web">www.TheQuillForge.com</div>
</div>

<div class="logo-lockup">
  <div class="brand"><span class="brand-dot"></span>Quill Forge Solutions</div>
</div>

</body>
</html>
```